Instagram background for quotes

We need a 1080x1080 background for instagram. I use the Letrova app to put text over the image.

We create motivating and inspiring messages for our followers on IG.

Our brands message is, "Mediocre thinking leads to mediocre results. Get Mission - Get Motivated - Get Moving
https://www.instagram.com/steel_outlook/

We would like to move away from the rustic look and have a gloss black background with the goal of using text that is cleaner to match the SO in the logo.

I see the design remaining fairly close to what it is now with the logo at the top. I like the quotes on this brand here, https://www.instagram.com/quizatycoon/?hl=en. I see this being built into our new background with the quotations being aggressive to match the wings in our logo.

Here is another brand we like - https://www.instagram.com/zipzapdrive/

I've attached the files I was given by the logo designer who has disappeared. I am hoping what is there will suffice.

Target Market(s)

24-34 year old males

Industry/Entity Type

Quotes

Colors
000000
ffffff

Requirements
Must have
• Provided Logo without text
Nice to have
• Aggressive looking quotes to match wings
• Watermark logo in background

```html
<!DOCTYPE html>
<html lang="en">
<head>
<meta charset="utf-8">
<title>Steel Outlook – Quote Background</title>
<link rel="stylesheet" href="https://fonts.googleapis.com/css2?family=Montserrat:wght@700&family=Rubik+Dirt&family=Exo+2:wght@600&display=swap">
<style>
  :root {
    --page: #ffffff;
    --ink: #000000;
    --light: #ffffff;
    --rule: #e6e6e6;
    --shadow: rgba(0, 0, 0, 0.45);
  }
  html, body {
    margin: 0;
    padding: 0;
    width: 1200px;
    height: 1200px;
    overflow: hidden;
    background: var(--page);
  }
  .canvas {
    position: relative;
    width: 1200px;
    height: 1200px;
  }
  .quote-card {
    position: absolute;
    left: 186px;
    top: 202px;
    width: 820px;
    height: 818px;
    background: var(--ink);
    box-shadow: 3px 3px 3px var(--shadow);
    overflow: hidden;
  }
  .brand-mark {
    position: absolute;
    top: 150px;
    left: 0;
    width: 100%;
    text-align: center;
    font-family: "Montserrat", sans-serif;
    font-weight: 700;
    color: var(--light);
    line-height: 1;
  }
  .brand-mark__top {
    display: block;
    font-size: 30px;
    letter-spacing: 3px;
  }
  .brand-mark__bottom {
    display: block;
    margin-top: 6px;
    font-size: 18px;
    letter-spacing: 5px;
  }
  .quote-frame {
    position: absolute;
    inset: 0;
    width: 820px;
    height: 818px;
  }
  .quote-frame__rule {
    stroke: var(--rule);
    stroke-width: 2;
    fill: none;
  }
  .quote-frame__mark {
    fill: var(--light);
  }
  .quote-text {
    position: absolute;
    left: 78px;
    top: 312px;
    width: 662px;
    margin: 0;
    text-align: center;
    font-family: "Rubik Dirt", sans-serif;
    font-size: 60px;
    line-height: 64px;
    color: var(--light);
  }
  .hashtag {
    position: absolute;
    left: 0;
    top: 744px;
    width: 100%;
    text-align: center;
    font-family: "Exo 2", sans-serif;
    font-weight: 600;
    font-size: 30px;
    letter-spacing: 1px;
    color: var(--light);
    margin: 0;
  }
</style>
</head>
<body>
  <main class="canvas">
    <section class="quote-card">
      <div class="brand-mark">
        <span class="brand-mark__top">STEEL</span>
        <span class="brand-mark__bottom">OUTLOOK</span>
      </div>

      <svg class="quote-frame" viewBox="0 0 820 818" aria-hidden="true">
        <line class="quote-frame__rule" x1="146" y1="296" x2="740" y2="296"/>
        <line class="quote-frame__rule" x1="78" y1="326" x2="78" y2="562"/>
        <line class="quote-frame__rule" x1="78" y1="562" x2="650" y2="562"/>
        <line class="quote-frame__rule" x1="740" y1="296" x2="740" y2="530"/>

        <g class="quote-frame__mark" transform="translate(54 250)">
          <path d="M0 68 L0 38 Q0 8 30 0 L36 12 Q18 18 17 30 L38 30 L38 68 Z"/>
          <path transform="translate(46 0)" d="M0 68 L0 38 Q0 8 30 0 L36 12 Q18 18 17 30 L38 30 L38 68 Z"/>
        </g>
        <g class="quote-frame__mark" transform="translate(762 610) rotate(180)">
          <path d="M0 68 L0 38 Q0 8 30 0 L36 12 Q18 18 17 30 L38 30 L38 68 Z"/>
          <path transform="translate(46 0)" d="M0 68 L0 38 Q0 8 30 0 L36 12 Q18 18 17 30 L38 30 L38 68 Z"/>
        </g>
      </svg>

      <p class="quote-text">don’t allow other<br>people to dictate<br>your emotions.</p>

      <p class="hashtag">#STEELOUTLOOK</p>
    </section>
  </main>
</body>
</html>
```